Refresh look of our invoices (Excel spreadsheet which converts to PDF) to better match our new look

We have recently updated our Website and other marketing material with a new look and would like to refresh our invoice template so that it better matches our new look.  The template is an excel spreadsheet which we convert to a PDF to send out to our clients.
The main requirement is to incorporate the newer design colours and general look/feel to align with what is on our website www.tarvellgroup.com.au
It is extremely important that excel formula functionality and general layout are much the same although we are open to any design suggestions you might have.
Please note:
-Totals figures and news panel must remain on the first page
-We need full ability to edit embedded formulas and Excel spreadsheet is NOT to be password protected as we will only be using it internally.
-It is crucial that the second and subsequent pages can be extended (duplicated) internally to allow for larger multi page entries. Some of our clients invoices run up to 4/5 pages in length and we need the abilty to keep adding rows)
-possibility to add a "convert to PDF" button within the sheet which provides a 1 click solution to convert to PDF rather than the manual 2 step process to convert.... If that can be done, we would not want the "convert to PDF" button to show on final PDF converted version we issue to our customers.   Ideally, a single "convert to PDF and print first cover page only" in 1 single click button named 'convert to PDF & print' would be really handy.  -  (Just to explain why - we email out a PDF version of invoice to our clients and only print off first page with totals for our records)
The design for the first page can be different from the second & subsequent pages (eg first page can be more fancy with following pages more basic)

Finance Industry
Marketing

```html
<!DOCTYPE html>
<html lang="en">
<head>
<meta charset="utf-8">
<title>Referrer Commission Statement</title>
<link href="https://fonts.googleapis.com/css2?family=Arimo:wght@400;700&display=swap" rel="stylesheet">
<style>
:root{
  --brand-green:#78c12a;
  --brand-ink:#2b2f2a;
  --head-green:#c4d79b;
  --grid:#a6a6a6;
  --row-alt:#f2f2f2;
  --rule:#c8c8c8;
  --dark-bar:#3f3f3f;
  --fee-red:#e00000;
  --text:#000;
}
*{margin:0;padding:0;box-sizing:border-box}
html,body{width:1200px;height:1000px;overflow:hidden;background:#fff}
body{position:relative;font-family:"Arimo",Arial,sans-serif;color:var(--text)}

.brand{position:absolute;left:207px;top:227px;width:228px;height:48px;background:var(--brand-green);
  display:flex;align-items:center;padding-left:12px}
.brand-name{font-size:27px;font-weight:700;color:var(--brand-ink);letter-spacing:-0.5px}
.header-rule-thin{position:absolute;left:435px;top:256px;width:551px;height:1px;background:#dcdcdc}
.header-rule{position:absolute;left:207px;top:276px;width:780px;height:3px;background:var(--rule)}
.referrer-label{position:absolute;left:666px;top:261px;font-size:13px}
.referrer-name{position:absolute;right:215px;top:259px;font-size:14px;font-weight:700}

.ledger{position:absolute;left:207px;top:311px;width:780px;border-collapse:collapse;font-size:11px;table-layout:fixed}
.ledger th{background:var(--head-green);border:1px solid var(--grid);height:39px;font-size:12px;font-weight:700;text-align:center;line-height:16px}
.ledger th.client{text-align:left;padding-left:3px}
.ledger td{border:1px solid var(--grid);height:16.7px;padding:0 2px;text-align:right;white-space:nowrap;line-height:15px}
.ledger td.client{text-align:left}
.ledger td.lender{text-align:center}
.ledger tbody tr:nth-child(even) td{background:var(--row-alt)}

.fees-rule{position:absolute;left:207px;top:631px;width:780px;height:3px;background:var(--rule)}
.fee{position:absolute;left:210px;font-size:10.5px;color:var(--fee-red)}
.fee b{text-decoration:underline}
.fee u{text-decoration:underline}
.fee-val{position:absolute;font-size:12px;color:var(--fee-red);text-align:right}

.summary{position:absolute;left:207px;top:696px;width:781px;border-collapse:collapse;table-layout:fixed;border:2px solid var(--dark-bar)}
.summary th{background:var(--dark-bar);color:#fff;font-size:12px;font-weight:700;height:23px;text-align:center}
.summary td{background:var(--row-alt);height:35px;font-size:12px;font-weight:700;text-align:center;border-left:1px solid #d0d0d0;border-bottom:2px solid #c0c0c0}
.summary td.neg{color:var(--fee-red)}
</style>
</head>
<body>
<div class="brand"><span class="brand-name">TARVELL GROUP</span></div>
<div class="header-rule-thin"></div>
<div class="header-rule"></div>
<div class="referrer-label">Referrer Name</div>
<div class="referrer-name">Daniel Brookes</div>

<table class="ledger">
<colgroup><col style="width:86px"><col style="width:64px"><col style="width:107px"><col style="width:106px"><col style="width:93px"><col style="width:102px"><col style="width:93px"><col style="width:129px"></colgroup>
<thead><tr><th class="client">Client</th><th>Lender</th><th>Loan<br>Amount</th><th>Upfront</th><th>Trail</th><th>Adj.</th><th>GST</th><th>TOTAL</th></tr></thead>
<tbody>
<tr><td class="client">dsgfg</td><td class="lender">Coralbank</td><td>$34,500.00</td><td>$0.00</td><td>$3.48</td><td>$0.00</td><td>$0.35</td><td>$3.83</td></tr>
<tr><td class="client">ggffgfd</td><td class="lender">Coralbank</td><td>$1,32,583.00</td><td>$0.00</td><td>$13.51</td><td>$0.00</td><td>$1.35</td><td>$14.86</td></tr>
<tr><td class="client">fggfdfg</td><td class="lender">Coralbank</td><td>$1,19,988.00</td><td>$0.00</td><td>$12.23</td><td>$0.00</td><td>$1.22</td><td>$13.45</td></tr>
<tr><td class="client">gfdfg</td><td class="lender">Coralbank</td><td>$4,79,999.00</td><td>$0.00</td><td>$48.92</td><td>$0.00</td><td>$4.89</td><td>$53.81</td></tr>
<tr><td class="client">dfg</td><td class="lender">Coralbank</td><td>$1,34,161.00</td><td>$0.00</td><td>$13.67</td><td>$0.00</td><td>$1.37</td><td>$15.04</td></tr>
<tr><td class="client">gdfg</td><td class="lender">Coralbank</td><td>$78,927.00</td><td>$0.00</td><td>$8.05</td><td>$0.00</td><td>$0.81</td><td>$8.86</td></tr>
<tr><td class="client">dffdgvfgf</td><td class="lender">Coralbank</td><td>$1,49,400.00</td><td>$0.00</td><td>$15.22</td><td>$0.00</td><td>$1.52</td><td>$16.74</td></tr>
<tr><td class="client">fgdg</td><td class="lender">Coralbank</td><td>$99,805.00</td><td>$0.00</td><td>$10.17</td><td>$0.00</td><td>$1.02</td><td>$11.19</td></tr>
<tr><td class="client">ffgdggf</td><td class="lender">Coralbank</td><td>$3,77,100.00</td><td>$0.00</td><td>$38.43</td><td>$0.00</td><td>$3.84</td><td>$42.27</td></tr>
<tr><td class="client">df</td><td class="lender">Coralbank</td><td>$1,01,738.00</td><td>$0.00</td><td>$10.37</td><td>$0.00</td><td>$1.04</td><td>$11.41</td></tr>
<tr><td class="client">gdgsdgsdf</td><td class="lender">Coralbank</td><td>$50,564.00</td><td>$0.00</td><td>$5.15</td><td>$0.00</td><td>$0.52</td><td>$5.67</td></tr>
<tr><td class="client">dsfggddfg</td><td class="lender">Coralbank</td><td>$1,08,500.00</td><td>$0.00</td><td>$7.38</td><td>$0.00</td><td>$0.74</td><td>$8.12</td></tr>
<tr><td class="client">dfdfgdsfghfd</td><td class="lender">Coralbank</td><td>$2,30,807.00</td><td>$0.00</td><td>$15.68</td><td>$0.00</td><td>$1.57</td><td>$17.25</td></tr>
<tr><td class="client">dfdjsf</td><td class="lender">OBK</td><td>$6,00,000.00</td><td>$4,000.00</td><td>$0.00</td><td>$0.00</td><td>$300.00</td><td>$4,300.00</td></tr>
</tbody>
</table>

<div class="fees-rule"></div>
<div class="fee" style="top:648px"><b>Software Fee</b> of $50 (+GST) - only applies in months with a new settlement occurring</div>
<div class="fee" style="top:664px"><b>Admin Fee</b> of $50 (+GST) - deducted from trail if <u>no new deals within last 6 months</u></div>
<div class="fee-val" style="top:647px;right:439px">-$50.00</div>
<div class="fee-val" style="top:647px;right:344px">-$5.00</div>
<div class="fee-val" style="top:647px;right:216px">-$55.00</div>
<div class="fee-val" style="top:664px;right:439px">$0.00</div>
<div class="fee-val" style="top:664px;right:344px">$0.00</div>
<div class="fee-val" style="top:664px;right:216px">$0.00</div>

<table class="summary">
<colgroup><col style="width:150px"><col style="width:107px"><col style="width:106px"><col style="width:93px"><col style="width:102px"><col style="width:93px"><col style="width:130px"></colgroup>
<thead><tr><th></th><th>Loan Book</th><th>Upfront</th><th>Trail</th><th>Adj.</th><th>GST</th><th>TOTAL</th></tr></thead>
<tbody><tr><td style="border-left:0"></td><td>$26,98,072.00</td><td>$4,000.00</td><td>$202.26</td><td class="neg">-$50.00</td><td>$315.24</td><td>$4,467.50</td></tr></tbody>
</table>
</body>
</html>
```